Flyer for an pediatric sleep consultancy - to distribute to play and childcare centers etc.

I need a flyer that will attract the attention of parents with children between the age of babies to toddlers, who may be experiencing sleep issues. The flyer will be placed at places such as community centers, doctors room, play centers, kindergardens, etc.

My company is called "The Quiet Meadow Studio" and provides a sleep consultancy service. My service essentially provides a customized plan for parents to follow and general advice and guidance. It is not medical advice.

I like to the flyer to have an overall tone that is soft and peaceful with a clean and beautiful design, however can catch the attention of parents who may be struggling with their child's sleep issues and are sleep deprived. I would like photos with minimal text. The colour I use is a brownish rose. I will attach some of my designs to give you an idea. You can have a look at my homepage as well to get an idea about my esthetic direction and the colour. Although the colour of my page is a bit too brownish....

I will provide the text to appear in the flyer once I have a better idea of the layout that I prefer for the flyer. The text however wont be extensive, just some catchy points.

I want to direct people to my website which is www.quietmeadowstudio-example.com
I offer a first FREE evaluation call, to the parents, to get to know each other better, learn about their child's particular sleep problems and see if we are a good fit and can work together. I would like to have this information somehow on the flyer, so that the parents will contact me.
I also have a facebook page, which is: The Quiet Meadow Studio

I have a logo that I would like to appear on the flyer. I will attach the file once the uploader on art bazaar is fixed.

When I print the flyer - I like to print A5 SIZE ... please make sure the formatting is OK for this size.

Here are some text ideas. of course all of it would be too much, I guess. On the front of the flyer I would like to have some catchy phrase or something similar to get people interested and to want to know more. On the back there could be a bit more text and information. But I'm open too suggestions....
I'm not too sure about the wording yet. But here are some text that I might be use:

Is sleep an issue in your home?

Is your baby having trouble sleeping? ... are you?!
I can help!

Sleep, baby, sleep….

Teaching children how to sleep

The Quiet Meadow Studio is a pediatric sleep consultancy that specializes in helping parents with children who struggle to develop good and healthy sleep habits.
Disruptive sleep patterns or not enough sleep can affect the physical, mental and emotional development of your child.

Of course nobody plans to have a sleep problem, but habits can become easily ingrained and spiral quickly out of control and you can find yourself sleep deprived, desperate and not too sure what to do. You see all the other sleeping babies and wish there was someone who understood what you were going through?! Well, there is!

Contact me for a free 15 minute consultation.

This 15 minute „mini“ consultation is a chance to discuss your unique sleep challenges and sleep goals with me. I will provide you with an overview of how I will work with your family to achieve your wildest sleep dreams (goals).
Furthermore do I understand and believe that every child and their family is unique and there is no one size fits all!
I would love to have a chat with you and talk about how I can help make things easier for you and your family!

Do I need a sleep consultant for my child?
The answer is yes if:
- if your child will only fall asleep when nursing or bottle feeding
- if your child needs a dummy or other external aid, like being rocked, patted or taken for a care ride to fall asleep
- if your good night routine is a challenging and exhausting procedure instead of a relaxed and enjoyable moment for the whole family
- if sleep is a constant battle in your home which leaves you feeling frustrated and exhausted
- if your own lack of sleep is taking a toll on you and the whole family

What can I do for you?

I will:

- Guide you to set an age appropriate foundation for good sleep
- Create an individual sleep plan tailored especially to your child’s sleep needs and circumstances
- Help you to teach your childto go to sleep and get back to sleep independently during the night
- show you how to teach your child to take healthful, restorative naps
-Learn

Contact:

Marta Lindqvist
info@quietmeadowstudio-example.com
www.quietmeadowstudio-example.com
+34 612 380 574

Consultations in English, German or Spanish via Phone/Skype or home consultation

Reason: I have to go on a business trip and won't be able to choose a design until the deadline. During the trip I won't have time to give feedback and ask for changes. thank you

Target Market(s)

parents, sleep deprived mothers, young families, child care provider,

Industry/Entity Type

Baby Care

Contact Information for Business Card

Marta Lindqvist
pediatric sleep consultant
+34 612 380 574

```html
<!DOCTYPE html>
<html lang="en">
<head>
<meta charset="utf-8">
<title>The Quiet Meadow Studio – A5 Flyer</title>
<link href="https://fonts.googleapis.com/css2?family=Libre+Baskerville:wght@400;700&family=Open+Sans:wght@300;400;600;700&family=Tinos&display=swap" rel="stylesheet">
<style>
  :root {
    --rose: #c98b7f;
    --rose-text: #c97f72;
    --sage: #7e8d8a;
    --ink: #2f2f2f;
    --paper: #ffffff;
    --backdrop: #2b2b2d;
    --rule: #c9a39a;
  }
  * { box-sizing: border-box; margin: 0; padding: 0; }
  html, body { width: 1200px; height: 800px; overflow: hidden; }
  body { background: var(--backdrop); font-family: "Open Sans", sans-serif; position: relative; }

  .flyer { position: absolute; width: 454px; height: 644px; background: var(--paper); overflow: hidden; }
  .flyer--front { left: 143px; top: 77px; }
  .flyer--back { left: 645px; top: 75px; display: flex; flex-direction: column; }

  /* Front */
  .front-photo { position: absolute; left: 0; top: 100px; width: 454px; height: 544px;
    background: linear-gradient(180deg, #d9dde2 0%, #e4e6e9 30%, #c9a48f 48%, #eeeeef 62%, #ffffff 88%); }
  .front-band { position: absolute; left: 0; top: 0; width: 454px; height: 150px; }
  .front-title { position: absolute; top: 36px; width: 100%; text-align: center;
    font-family: "Libre Baskerville", serif; font-weight: 700; color: #fff; font-size: 36px; letter-spacing: 0.5px; }
  .front-sub { position: absolute; top: 77px; left: 27px; right: 27px; display: flex; align-items: center; gap: 10px;
    font-family: "Libre Baskerville", serif; color: #fff; font-size: 17px; }
  .front-sub::before, .front-sub::after { content: ""; flex: 1; height: 1px; background: #fff; }
  .front-brand { position: absolute; top: 548px; width: 100%; text-align: center;
    font-weight: 300; color: var(--sage); font-size: 25px; letter-spacing: -0.3px; }

  /* Back */
  .back-header { position: relative; flex: none; height: 104px; }
  .back-band { position: absolute; left: 0; top: 0; width: 454px; height: 95px; }
  .back-brand { position: absolute; top: 40px; width: 100%; text-align: center;
    font-weight: 300; color: var(--sage); font-size: 15px; }

  .intro { flex: none; padding: 0 10px 0 17px; }
  .intro-item { display: flex; gap: 10px; align-items: center; margin-bottom: 6px;
    color: var(--rose-text); font-size: 9.4px; line-height: 12.6px; letter-spacing: -0.1px; }
  .intro-item .chev { color: var(--ink); font-size: 10px; width: 10px; flex: none; }
  .cta { color: var(--sage); font-weight: 700; font-size: 12px; margin: 8px 0 8px 20px; }

  .columns { position: relative; flex: none; display: flex; padding: 4px 0 0 28px; }
  .col { font-size: 8.5px; line-height: 11px; color: var(--ink); letter-spacing: -0.05px; }
  .col--need { width: 206px; }
  .col--offer { width: 192px; margin-left: 20px; }
  .col h3 { font-size: 9.8px; font-weight: 600; line-height: 13px; margin-bottom: 8px; }
  .col--offer h3 { margin-top: 7px; margin-bottom: 14px; }
  .col p.lead { margin-bottom: 4px; }
  .col ul { list-style: none; }
  .col li { position: relative; padding-left: 16px; margin-bottom: 5px; }
  .col li::before { content: ""; position: absolute; left: 0; top: 50%; width: 6px; height: 6px; margin-top: -3px;
    border-radius: 50%; background: var(--rose); }
  .divider { position: absolute; left: 236px; top: 34px; width: 12px; height: 168px; }

  .footer { flex: none; margin-top: auto; padding: 0 17px 10px; }
  .rule { height: 1px; background: var(--rule); margin-bottom: 6px; }
  .contact-name { padding-left: 10px; color: var(--rose-text); font-weight: 600; font-size: 17px; line-height: 22px; }
  .contact-note { padding-left: 10px; font-size: 7.2px; color: var(--ink); margin-bottom: 8px; }
  .contact-grid { display: grid; grid-template-columns: 217px 1fr; row-gap: 7px; padding-left: 11px; }
  .contact { display: flex; align-items: flex-start; gap: 8px;
    font-family: "Tinos", serif; font-size: 10.6px; color: var(--ink); line-height: 12.5px; }
  .contact svg { flex: none; }
</style>
</head>
<body>

<section class="flyer flyer--front">
  <div class="front-photo" role="img" aria-label="Photograph of a toddler peeking over a soft white blanket"></div>
  <svg class="front-band" viewBox="0 0 454 150" preserveAspectRatio="none">
    <path d="M0 0 H454 V110 Q300 146 0 116 Z" fill="#fff"/>
    <path d="M0 0 H454 V98 Q300 140 0 108 Z" fill="var(--rose)"/>
  </svg>
  <h1 class="front-title">IS SLEEP AN ISSUE</h1>
  <p class="front-sub">IN YOUR HOME?</p>
  <p class="front-brand">The Quiet Meadow Studio</p>
</section>

<section class="flyer flyer--back">
  <header class="back-header">
    <svg class="back-band" viewBox="0 0 454 95" preserveAspectRatio="none">
      <path d="M0 62 Q220 118 454 40 V50 Q220 128 0 76 Z" fill="var(--rose)"/>
    </svg>
    <p class="back-brand">The Quiet Meadow Studio</p>
  </header>

  <div class="intro">
    <p class="intro-item"><span class="chev">»</span><span>The Quiet Meadow Studio is a pediatric sleep consultancy that specializes in helping parents with children who struggle to develop good and healthy sleep habits.</span></p>
    <p class="intro-item"><span class="chev">»</span><span>Disruptive sleep patterns or not enough sleep can affect the phyical, mental and emotional development of your child.</span></p>
    <p class="intro-item"><span class="chev">»</span><span>Of course nobody plans to have a sleep problem, but habits can become easily ingrained and spiral quickly out of control and you can find yourself sleep deprived, desperate and not too sure what to do. You see all the other sleeping babies and wish there was someone who understood what you were going through?! Well, there is!</span></p>
    <p class="cta">CONTACT ME FOR A FREE 15 MINUTE CONSULTATION.</p>
    <p class="intro-item"><span class="chev">»</span><span>This 15 minute „mini“ consultation is a chance to discuss your unique sleep challenges and sleep goals with me. I will provide you with an overview of how I will work with your family to achieve your wildest sleep dreams (goals). Furthermore do I understand and believe that every child and their family is unique and there is no one size fits all!I would love to have a chat with you and talk about how I can help make things easier for you and your family!</span></p>
  </div>

  <div class="columns">
    <div class="col col--need">
      <h3>Do I Need A Sleep Consultant For My Child?</h3>
      <p class="lead">The answer is yes if:</p>
      <ul>
        <li>if your child will only fall asleep when nursing or bottle feeding</li>
        <li>if your child needs a dummy or other external aid, like being rocked, patted or taken for a care ride to fall asleep</li>
        <li>if your good night routine is a challenging and exhausting procedure instead of a relaxe and enjoyable moment for the whole family</li>
        <li>if sleep is a constant battle in your home leaves you feeling frustrated and exhausted</li>
        <li>if your own lack of sleep is taking a toll on you and the whole family</li>
      </ul>
    </div>
    <div class="col col--offer">
      <h3>What can I do for you?</h3>
      <p class="lead">I will:</p>
      <ul>
        <li>Guide you to set an age appropriate foundation for good sleep</li>
        <li>Create an individual sleep plan tailored especially to your child’s sleep needs and circumstances</li>
        <li>Help you to teach your childto go to sleep and get back to sleep independently during the night</li>
        <li>show you how to teach your child to take healthful, restorative naps</li>
        <li>Learn</li>
      </ul>
    </div>
    <svg class="divider" viewBox="0 0 12 168">
      <line x1="1" y1="0" x2="1" y2="168" stroke="#bbb" stroke-width="1"/>
      <path d="M1 70 L12 79 L1 88 Z" fill="var(--rose)"/>
    </svg>
  </div>

  <footer class="footer">
    <div class="rule"></div>
    <p class="contact-name">Marta Lindqvist</p>
    <p class="contact-note">Consultations In English, German Or Spanish Via Phone/skype Or Home Consultation</p>
    <div class="contact-grid">
      <p class="contact">
        <svg width="13" height="13" viewBox="0 0 14 14"><circle cx="7" cy="7" r="6.3" fill="none" stroke="var(--rose)"/><path d="M4.6 4 l1.3-.3 .7 1.6-.8.6 a4 4 0 0 0 1.9 1.9 l.6-.8 1.6.7-.3 1.3 c-3 .2-5.2-2-5-5z" fill="var(--rose)"/></svg>
        +34 612 380 574
      </p>
      <p class="contact">
        <svg width="13" height="13" viewBox="0 0 14 14"><circle cx="7" cy="7" r="6.3" fill="none" stroke="var(--rose)"/><circle cx="7" cy="7" r="3.2" fill="none" stroke="var(--rose)" stroke-width=".9"/><path d="M3.8 7 H10.2 M7 3.8 V10.2" stroke="var(--rose)" stroke-width=".8"/></svg>
        www.quietmeadowstudio-example.com
      </p>
      <p class="contact">
        <svg width="13" height="13" viewBox="0 0 14 14"><circle cx="7" cy="7" r="6.3" fill="none" stroke="var(--rose)"/><rect x="4" y="5" width="6" height="4.2" fill="none" stroke="var(--rose)" stroke-width=".9"/><path d="M4 5 L7 7.4 L10 5" fill="none" stroke="var(--rose)" stroke-width=".9"/></svg>
        info@quietmeadowstudio-example.com
      </p>
      <p class="contact">
        <svg width="13" height="13" viewBox="0 0 14 14"><circle cx="7" cy="7" r="6.3" fill="none" stroke="var(--rose)"/><path d="M7 10.5 C5 8 4.7 7 4.7 6 a2.3 2.3 0 0 1 4.6 0 c0 1-.3 2-2.3 4.5z" fill="none" stroke="var(--rose)" stroke-width=".9"/><circle cx="7" cy="6" r=".8" fill="var(--rose)"/></svg>
        <span>Carrer de l'Exemple 12<br>08001 Barcelona</span>
      </p>
    </div>
  </footer>
</section>

</body>
</html>
```